Daily Care Record Sheets

As a preschool, we have notes that we send home on a daily basis so the parents know what is going on. We would like to reformat the preschool and toddler sheets<br/><br/>The preschool participation sheet is 4.25"x 5.6"<br/>We have attached an example of what we are using currently and the information we would like on our new sheet. We would like the logo added as well.<br/><br/>The Little Sprouts sheet should be a half page. I have included 2 examples as well as a sheet of what we would like on it moving forward. <br/><br/>Please do not hesitate to reach out if you have any questions on any of this. They will print in black and white on colored paper.<br/><br/>Thanks!<br/>Marla

Target Market(s)

Parents of the toddlers and preschools in our care

Industry/Entity Type

Preschool

Colors

Designer to choose only greyscale colors for use in the design.

Requirements
Must have
• Logo
• The items in the "FOR NEW VERSION" files

```html
<!DOCTYPE html>
<html lang="en">
<head>
<meta charset="utf-8">
<title>Little Sprouts – Daily Care Record</title>
<link rel="stylesheet" href="https://fonts.googleapis.com/css2?family=Oswald:wght@300;400;500&family=Roboto:wght@400&display=swap">
<style>
  :root {
    --ink: #000000;
    --paper: #ffffff;
    --rule: #333333;
    --grid: #555555;
    --text: #1a1a1a;
  }
  * { box-sizing: border-box; margin: 0; padding: 0; }
  html, body { width: 1200px; height: 848px; overflow: hidden; background: var(--paper); }
  .sheet { position: relative; width: 1200px; height: 848px; color: var(--text); font-family: "Oswald", sans-serif; }
  .abs { position: absolute; }

  .brand { left: 48px; top: 22px; display: flex; flex-direction: column; align-items: center; gap: 6px; }
  .brand-dot { width: 26px; height: 26px; border-radius: 50%; background: var(--ink); }
  .brand-name { font-family: "Roboto", sans-serif; font-size: 24px; color: var(--ink); letter-spacing: -0.3px; }

  .field-label { font-size: 16px; font-weight: 500; color: var(--ink); top: 38px; }
  .field-line { height: 0; border-top: 1.2px solid var(--rule); top: 62px; }

  .title-band { left: 0; top: 92px; width: 1200px; height: 48px; background: var(--ink); color: var(--paper);
    display: flex; align-items: center; justify-content: center; font-size: 26px; font-weight: 500; letter-spacing: 0.5px; text-transform: uppercase; }

  .icon { width: 40px; height: 40px; }

  .card { border: 1.4px solid var(--ink); border-radius: 10px; overflow: hidden; background: var(--paper); }
  .card-head { background: var(--ink); color: var(--paper); height: 31px; display: flex; align-items: center; justify-content: center;
    font-family: "Roboto", sans-serif; font-size: 18px; }

  .meal { top: 204px; width: 143px; height: 236px; }
  .meal-options { list-style: none; text-align: center; font-weight: 300; font-size: 19px; padding-top: 20px; }
  .meal-options li { height: 45px; line-height: 22px; }

  .disposition { left: 61px; top: 499px; width: 508px; height: 155px; }
  .mood { position: absolute; font-weight: 300; font-size: 19px; transform: translateX(-50%); }

  .nap { left: 61px; top: 710px; width: 508px; height: 110px; }
  .nap-choice { position: absolute; top: 55px; font-weight: 300; font-size: 19px; transform: translateX(-50%); white-space: nowrap; }

  .toileting { left: 634px; top: 204px; width: 507px; height: 294px; }
  .log-grid { position: absolute; left: 0; top: 31px; display: grid;
    grid-template-columns: 62px 103px 71px 109px; grid-template-rows: repeat(7, 37px); }
  .log-grid span { border-right: 1px solid var(--grid); border-bottom: 1px solid var(--grid);
    font-family: "Roboto", sans-serif; font-size: 13px; display: flex; align-items: center; padding-left: 7px; }
  .log-grid span:nth-last-child(-n+4) { border-bottom: none; }
  .legend { position: absolute; left: 345px; top: 31px; width: 160px; height: 261px; border-left: 1px solid var(--grid); }
  .legend-row { position: absolute; left: 20px; display: flex; font-size: 13px; }
  .legend-row b { width: 36px; font-weight: 500; font-size: 15px; }
  .legend-row i { font-style: normal; font-family: "Roboto", sans-serif; font-size: 12.5px; line-height: 1.35; }

  .note-label { left: 631px; font-size: 16px; font-weight: 500; color: var(--ink); }
  .note-line { left: 634px; width: 507px; border-top: 1.2px solid var(--rule); }
</style>
</head>
<body>
<main class="sheet">
  <header>
    <div class="abs brand">
      <div class="brand-name"><span class="brand-dot" style="display:inline-block;vertical-align:middle;margin-right:8px;width:20px;height:20px"></span>Maple Grove Academy</div>
    </div>
    <div class="abs field-label" style="left:614px">CHILD:</div>
    <div class="abs field-line" style="left:654px;width:248px"></div>
    <div class="abs field-label" style="left:948px">DATE:</div>
    <div class="abs field-line" style="left:986px;width:172px"></div>
  </header>

  <h1 class="abs title-band">Little Sprouts</h1>

  <!-- meals -->
  <svg class="abs icon" style="left:112px;top:156px" viewBox="0 0 40 40" role="img" aria-label="Meal icon"><circle cx="20" cy="20" r="19" fill="var(--ink)"/><path d="M14 10v8M12 10v7q0 3 2.5 3.5V31M17 10v7q0 3-2.5 3.5" stroke="#fff" stroke-width="1.6" fill="none"/><path d="M25 10q4 3 3 11h-3V31" stroke="#fff" stroke-width="2" fill="none"/></svg>
  <svg class="abs icon" style="left:295px;top:156px" viewBox="0 0 40 40" role="img" aria-label="Meal icon"><circle cx="20" cy="20" r="19" fill="var(--ink)"/><path d="M14 10v8M12 10v7q0 3 2.5 3.5V31M17 10v7q0 3-2.5 3.5" stroke="#fff" stroke-width="1.6" fill="none"/><path d="M25 10q4 3 3 11h-3V31" stroke="#fff" stroke-width="2" fill="none"/></svg>
  <svg class="abs icon" style="left:477px;top:156px" viewBox="0 0 40 40" role="img" aria-label="Meal icon"><circle cx="20" cy="20" r="19" fill="var(--ink)"/><path d="M14 10v8M12 10v7q0 3 2.5 3.5V31M17 10v7q0 3-2.5 3.5" stroke="#fff" stroke-width="1.6" fill="none"/><path d="M25 10q4 3 3 11h-3V31" stroke="#fff" stroke-width="2" fill="none"/></svg>

  <section class="abs card meal" style="left:61px">
    <div class="card-head">A.M. SNACK</div>
    <ul class="meal-options"><li>ALL</li><li>MOST</li><li>SOME</li><li>NONE</li></ul>
  </section>
  <section class="abs card meal" style="left:244px">
    <div class="card-head">LUNCH</div>
    <ul class="meal-options"><li>ALL</li><li>MOST</li><li>SOME</li><li>NONE</li></ul>
  </section>
  <section class="abs card meal" style="left:426px">
    <div class="card-head">P.M. SNACK</div>
    <ul class="meal-options"><li>ALL</li><li>MOST</li><li>SOME</li><li>NONE</li></ul>
  </section>

  <!-- disposition -->
  <svg class="abs icon" style="left:292px;top:453px" viewBox="0 0 40 40" role="img" aria-label="Disposition icon"><circle cx="20" cy="20" r="19" fill="var(--ink)"/></svg>
  <section class="abs card disposition">
    <div class="card-head">DISPOSITION</div>
    <span class="mood" style="left:71px;top:57px">HAPPY</span>
    <span class="mood" style="left:183px;top:57px">FRIENDLY</span>
    <span class="mood" style="left:311px;top:57px">CHEERFUL</span>
    <span class="mood" style="left:427px;top:57px">QUIET</span>
    <span class="mood" style="left:71px;top:101px">CURIOUS</span>
    <span class="mood" style="left:183px;top:101px">SLEEPY</span>
    <span class="mood" style="left:311px;top:101px">ENERGETIC</span>
    <span class="mood" style="left:427px;top:101px">TALKATIVE</span>
  </section>

  <!-- nap -->
  <svg class="abs icon" style="left:292px;top:664px" viewBox="0 0 40 40" role="img" aria-label="Nap time moon icon"><circle cx="20" cy="20" r="19" fill="var(--ink)"/><path d="M22 9a11 11 0 1 0 9 16a9 9 0 1 1-9-16z" fill="#fff"/></svg>
  <section class="abs card nap">
    <div class="card-head">NAP TIME</div>
    <span class="nap-choice" style="left:77px">2 HOURS</span>
    <span class="nap-choice" style="left:229px">1 HOUR 30 MINUTES</span>
    <span class="nap-choice" style="left:407px">I WASN'T SLEEPY</span>
  </section>

  <!-- toileting -->
  <svg class="abs icon" style="left:864px;top:158px" viewBox="0 0 40 40" role="img" aria-label="Diaper and toileting icon"><circle cx="20" cy="20" r="19" fill="var(--ink)"/></svg>
  <section class="abs card toileting">
    <div class="card-head">DIAPER/TOILETING</div>
    <div class="log-grid">
      <span>6:30 am</span><span></span><span>1:00 pm</span><span></span>
      <span>7:00 am</span><span></span><span>2:00 pm</span><span></span>
      <span>8:00 am</span><span></span><span>3:00 pm</span><span></span>
      <span>9:00 am</span><span></span><span>4:00 pm</span><span></span>
      <span>10:00 am</span><span></span><span>5:00 pm</span><span></span>
      <span>11:00 am</span><span></span><span>6:00 pm</span><span></span>
      <span>12:00 nn</span><span></span><span></span><span></span>
    </div>
    <div class="legend">
      <div class="legend-row" style="top:25px"><b>D</b><i>Dry</i></div>
      <div class="legend-row" style="top:62px"><b>W</b><i>Wet</i></div>
      <div class="legend-row" style="top:99px"><b>BM</b><i>Bowel Movement</i></div>
      <div class="legend-row" style="top:136px"><b>P</b><i>Pee on toilet</i></div>
      <div class="legend-row" style="top:173px"><b>T</b><i>Tried toilet</i></div>
      <div class="legend-row" style="top:210px"><b>BMT</b><i>Bowel Movement<br>on toilet</i></div>
    </div>
  </section>

  <!-- notes -->
  <div class="abs note-label" style="top:545px">YOUR CHILD NEEDS:</div>
  <div class="abs note-line" style="top:595px"></div>
  <div class="abs note-label" style="top:626px">TODAY I HAD FUN:</div>
  <div class="abs note-line" style="top:676px"></div>
  <div class="abs note-label" style="top:710px">NOTES/REMINDERS:</div>
  <div class="abs note-line" style="top:761px"></div>
  <div class="abs note-line" style="top:802px"></div>
</main>
</body>
</html>
```